依頼詳細
【暖簾(のれん)】のデザインを依頼させて頂きます。

店名やお店の雰囲気が、見てすぐにわかるようなデザインを希望します。

男女問わず、幅広い年齢層の方が来店されますので、
入店したいと思って頂けるよう、
分かりやすく、ほっこりくつろげる雰囲気でお願いします。
記載項目
◆サイズ:幅130センチ × 丈80センチ
※三枚に割れる形です。

◆文字色:3色まで。
フォント:レトロ系・ほっこり系(堅苦しくないもの)

◆イラスト可

◆お店の名前を、分かりやすくいれてください。
漢字以外を希望(ねむか・ネムカ どちらでも)

◆イチオシメニューを入れてください。(散りばめ可)(一部・複数可)
・もつ鍋
・馬刺し
・串焼き
・串かつ
・梅酒
・ネルカス
・地酒
・焼酎
希望イメージ
シンプル 複雑
単色 カラフル
暗い 明るい
日常 高級
遊び心 厳粛
未来的 伝統的
女性的 男性的
希望する色
【生地色】生成り or えんじ色   【文字色】落ち着いた色
納品ファイル
• 高解像度JPG (.jpg)
• イラストレーター形式 (.ai)
• PNG形式 (.png)

```html
<!DOCTYPE html>
<html lang="ja">
<head>
<meta charset="utf-8">
<title>ねむか 暖簾</title>
<link rel="stylesheet" href="https://fonts.googleapis.com/css2?family=Dela+Gothic+One&family=Yusei+Magic&display=swap">
<style>
  :root {
    --cloth-red: #c9343e;
    --indigo: #1d1b80;
    --paper: #ffffff;
    --ink-light: #ffffff;
    --name-red: #d8404a;
  }
  html, body {
    margin: 0;
    padding: 0;
    overflow: hidden;
    background: var(--paper);
  }
  .canvas {
    position: relative;
    width: 847px;
    height: 1200px;
    background: var(--paper);
    overflow: hidden;
  }
  .noren {
    position: absolute;
    left: 0;
    width: 847px;
    background: var(--cloth-red);
  }
  .noren--white-name { top: 0; height: 566px; }
  .noren--red-name { top: 673px; height: 527px; }

  .menu-left,
  .menu-right {
    position: absolute;
    writing-mode: vertical-rl;
    color: var(--ink-light);
    font-family: "Yusei Magic", sans-serif;
    line-height: 1;
    white-space: nowrap;
  }
  .menu-left {
    left: 172px;
    font-size: 52px;
    letter-spacing: 0;
  }
  .menu-right {
    left: 645px;
    font-size: 36px;
    letter-spacing: 0.5px;
  }
  .noren--white-name .menu-left,
  .noren--white-name .menu-right { top: 99px; }
  .noren--red-name .menu-left,
  .noren--red-name .menu-right { top: 67px; }

  .sign-board {
    position: absolute;
    left: 268px;
    width: 325px;
    height: 325px;
    background: var(--indigo);
    display: flex;
    align-items: center;
    justify-content: center;
  }
  .noren--white-name .sign-board { top: 99px; }
  .noren--red-name .sign-board { top: 67px; }

  .shop-name {
    font-family: "Dela Gothic One", sans-serif;
    font-size: 92px;
    line-height: 1;
    letter-spacing: -2px;
  }
  .shop-name--white { color: var(--ink-light); }
  .shop-name--red { color: var(--name-red); }
</style>
</head>
<body>
<div class="canvas">
  <section class="noren noren--white-name">
    <div class="menu-left">全国各地の梅酒</div>
    <div class="sign-board"><span class="shop-name shop-name--white">ねむか</span></div>
    <div class="menu-right">もつ鍋・馬刺し・串焼き</div>
  </section>

  <section class="noren noren--red-name">
    <div class="menu-left">全国各地の梅酒</div>
    <div class="sign-board"><span class="shop-name shop-name--red">ねむか</span></div>
    <div class="menu-right">もつ鍋・馬刺し・串焼き</div>
  </section>
</div>
</body>
</html>
```